Peter Lasko-Wren Finance

Need a personal website Kestrel Equipment Finance,Business Finance,Commercial Finance, Construction Finance, Bridging Finance. Similar websites are www.varoplend.com.au / www.kitmoxa.com.au / www.rzb4.com.au /wwwbelvaxcredit.com.au

Target Market(s)

Business People

Industry/Entity Type

Business

Number of Pages Required

3 page

Font styles to use
Serif
Sans Serif

Requirements
Must have
• All i want is a simple corporate looking website Kestrel Equipment Finance, Commercial Finance, Construction Finance, Business Finance, Bridging Finance,

```html
<!DOCTYPE html>
<html lang="en">
<head>
<meta charset="utf-8">
<title>Kestrel Equipment – Equipment Finance</title>
<link rel="stylesheet" href="https://fonts.googleapis.com/css2?family=Roboto:wght@300;400;500;700&family=Roboto+Slab:wght@400;500&display=swap">
<style>
:root{
  --blue:#27a3dd;
  --blue-dark:#1b8fc7;
  --green:#a6d22e;
  --navy:#1f3c57;
  --ink:#333;
  --muted:#666;
  --pale:#f3f4f6;
  --white:#fff;
  --sans:'Roboto',Arial,sans-serif;
  --serif:'Roboto Slab',Georgia,serif;
}
*{box-sizing:border-box;margin:0;padding:0}
html,body{width:1200px;height:3144px;overflow:hidden}
body{font-family:var(--sans);color:var(--ink);background:var(--white)}
.page{position:relative;width:1200px;height:3144px;overflow:hidden}
.abs{position:absolute}

/* header */
.topbar{left:690px;top:0;width:510px;height:40px;background:var(--blue);clip-path:polygon(30px 0,100% 0,100% 100%,0 100%)}
.topbar .mail{position:absolute;left:50px;top:11px;color:#fff;font-size:14px}
.social{display:flex;gap:8px}
.social i{display:block;width:24px;height:24px;border-radius:50%;background:#fff;opacity:.92}
.topbar .social{position:absolute;left:255px;top:8px}
.brand{display:flex;align-items:center;gap:10px}
.brand-mark{width:22px;height:22px;background:var(--blue)}
.brand-name{font-family:var(--sans);font-weight:500;font-size:18px;color:#222;white-space:nowrap}
.header-brand{left:130px;top:66px}
.nav{left:450px;top:82px;display:flex;gap:34px;font-size:13px;color:#444}
.nav .active{color:var(--blue);border-bottom:2px solid var(--blue);padding-bottom:4px}

/* hero */
.hero{left:0;top:120px;width:1200px;height:740px}
.hero-photo{position:absolute;inset:0;background:linear-gradient(100deg,#8a9aa5 0%,#c8d0d6 40%,#aeb9c2 65%,#7f8c95 100%)}
.hero svg{position:absolute;left:0;top:0}
.hero-copy{position:absolute;left:0;width:1200px;top:128px;text-align:center;color:#fff}
.hero-title{font-size:27px;font-weight:400;line-height:31px}
.hero-rule{width:300px;height:1px;background:rgba(255,255,255,.7);margin:12px auto 12px}
.hero-sub{font-size:14.5px;line-height:20px}
.btn{display:inline-block;font-size:14px;font-weight:500;text-align:center}
.btn-blue{background:var(--blue);color:#fff}
.hero .btn-blue{margin-top:16px;width:230px;height:46px;line-height:46px;font-size:16px}
.callback{position:absolute;left:0;width:1200px;top:552px;text-align:center;color:#fff}
.callback h2{font-family:var(--serif);font-weight:400;font-size:24px}
.field{position:absolute;top:603px;width:282px;height:38px;background:#fff;border-radius:2px;font-size:10px;color:#999;padding:12px 10px}
.cb-btn{position:absolute;top:658px;width:212px;height:46px;line-height:46px;border-radius:2px;font-size:14px;font-weight:500;text-align:center}

/* services */
.services{left:0;top:860px;width:1200px;height:390px;background:linear-gradient(180deg,#eef1f4,#f7f8fa 60%,#eff2f5)}
.section-title{font-family:var(--serif);font-weight:400;font-size:26px;color:#222;text-align:center}
.service{position:absolute;top:120px;width:230px;text-align:center}
.service .ring{width:82px;height:82px;border-radius:50%;border:3px solid var(--blue);margin:0 auto;display:flex;align-items:center;justify-content:center}
.service .ring span{width:62px;height:62px;border-radius:50%;background:var(--blue);display:flex;align-items:center;justify-content:center}
.service h3{color:var(--blue);font-weight:400;font-size:16px;margin-top:18px}
.service p{font-size:11px;line-height:15px;color:#444;margin-top:6px;padding:0 8px}
.divider{display:flex;align-items:center;justify-content:center;gap:6px;margin-top:14px}
.divider b{width:66px;height:2px;background:#bfc7cc}
.divider i{width:14px;height:14px;background:var(--green);color:#fff;font-style:normal;font-size:12px;line-height:14px}

/* testimonials */
.testimonials{left:0;top:1253px;width:1200px;height:372px;background:linear-gradient(110deg,#2c2d30,#1c1c1e 45%,#3a3b3d 70%,#161617)}
.testimonials .section-title{color:#fff;margin-top:34px}
.avatar{position:absolute;left:545px;top:104px;width:110px;height:110px;border-radius:50%;border:4px solid #ddd;background:linear-gradient(160deg,#a9b4bd,#5d6b76)}
.t-name{position:absolute;top:228px;width:1200px;text-align:center;color:var(--blue);font-size:12px;font-weight:500}
.t-role{position:absolute;top:246px;width:1200px;text-align:center;color:#ddd;font-size:10px}
.t-quote{position:absolute;left:225px;top:272px;width:750px;text-align:center;color:#eee;font-size:11px;line-height:15px}
.arrow{position:absolute;width:28px;height:28px;border-radius:50%}

/* finance tabs */
.lease{left:135px;top:1678px;width:488px;height:290px;background:#f7f7f8;padding:28px 10px 0 10px}
.lease h3{color:var(--blue);font-weight:400;font-size:17px}
.lease p{font-size:11.5px;line-height:17px;color:#555;margin-top:18px}
.btn-row{display:flex;gap:14px;margin-top:16px}
.btn-solid,.btn-outline{height:40px;line-height:38px;border-radius:2px;font-size:13px;font-weight:500;text-align:center}
.btn-solid{background:var(--blue);color:#fff;border:1px solid var(--blue)}
.btn-outline{background:#fff;color:var(--blue);border:2px solid var(--blue)}
.tabs{left:628px;top:1678px;width:437px;height:290px;background:#f7f7f8}
.tab-row{display:flex;height:54px;border-bottom:2px solid var(--blue)}
.tab-row span{flex:1;text-align:center;line-height:52px;font-size:14px;color:var(--blue);border:1px solid #ddd;border-bottom:none;background:#fff}
.tab-row .on{background:var(--blue);color:#fff;border-color:var(--blue)}
.tab-body{padding:22px 14px 0}
.tab-body p{font-size:11.5px;line-height:17px;color:#555}
.tab-body .links{color:var(--blue);margin-top:10px}

/* needs band */
.needs{left:0;top:2010px;width:1200px;height:300px;background:var(--blue)}
.needs-photo{position:absolute;left:-60px;top:-10px;width:400px;height:330px;border-radius:0 200px 200px 0;border:6px solid var(--green);border-left:none;background:linear-gradient(150deg,#eef1f4,#c3cbd2 55%,#5b6a78);overflow:hidden}
.needs-copy{position:absolute;left:370px;top:22px;width:760px;color:#fff}
.needs-copy h2{font-weight:400;font-size:22px}
.needs-copy p{font-size:12px;line-height:18px;margin-top:18px}
.needs-copy ul{list-style:none;margin-top:6px;font-size:12px;line-height:20px}
.needs-copy li::before{content:"›";color:var(--green);font-weight:700;margin-right:8px;font-size:15px}

/* clients */
.clients{left:0;top:2310px;width:1200px;height:305px}
.clients h2{font-family:var(--serif);font-weight:400;font-size:34px;color:var(--navy);text-align:center;margin-top:42px}
.client{position:absolute;width:190px;text-align:center;font-family:var(--sans);font-weight:500;font-size:16px;color:#444}

/* blog */
.blog{left:0;top:2615px;width:1200px;height:300px;background:var(--pale)}
.blog h2{font-family:var(--serif);font-weight:400;font-size:26px;color:var(--blue);text-align:center;margin-top:32px}
.post{position:absolute;top:110px;width:480px}
.date{position:absolute;left:0;top:0;width:126px;height:126px;border-radius:50%;background:var(--blue);border:5px solid #fff;box-shadow:-4px 4px 0 var(--green);color:#fff;text-align:center;padding-top:26px}
.date b{display:block;font-size:34px;font-weight:400;line-height:36px}
.date span{font-size:22px}
.post h4{margin-left:140px;font-size:14px;font-weight:700;color:#222}
.post p{margin-left:140px;margin-top:8px;font-size:11.5px;line-height:16px;color:#555}

/* footer */
.footer{left:0;top:2860px;width:1200px;height:284px}
.footer svg{position:absolute;left:0;top:0}
.footer-brand{position:absolute;right:620px;top:96px}
.footer-brand .brand-mark{background:var(--white)}
.footer-brand .brand-name{color:#fff;font-size:16px}
.f-divider{position:absolute;left:600px;top:62px;width:1px;height:100px;background:rgba(255,255,255,.5)}
.footer .social{position:absolute;left:628px;top:72px;gap:10px}
.footer .social i{width:32px;height:32px}
.f-mail{position:absolute;left:628px;top:128px;color:#fff;font-size:14px}
.f-rule{position:absolute;left:0;top:182px;width:1200px;height:1px;background:rgba(255,255,255,.35)}
.f-nav{position:absolute;top:203px;width:1200px;display:flex;justify-content:center;gap:42px;font-size:12px;line-height:16px;color:#fff}
.f-nav .active{color:#0d3550}
.f-rule2{position:absolute;left:0;top:242px;width:1200px;height:1px;background:rgba(255,255,255,.35)}
.copyright{position:absolute;top:257px;width:1200px;text-align:center;font-size:11px;color:#fff}
</style>
</head>
<body>
<div class="page">

  <!-- header -->
  <div class="abs topbar">
    <span class="mail">✉ info@kestrel-adequip.com</span>
    <div class="social"><i></i><i></i><i></i><i></i></div>
  </div>
  <div class="abs brand header-brand">
    <span class="brand-mark"></span>
    <span class="brand-name">Kestrel Equipment</span>
  </div>
  <nav class="abs nav">
    <span class="active">Home</span><span>Equipment Finance</span><span>Business Finance</span><span>Supplier Finance</span><span>Equip Blog</span><span>Contact Us</span>
  </nav>

  <!-- hero + callback -->
  <section class="abs hero">
    <div class="hero-photo" role="img" aria-label="Photo of business people shaking hands in a bright office"></div>
    <svg width="1200" height="740" viewBox="0 0 1200 740" aria-hidden="true">
      <path d="M0,362 Q560,640 1200,330 L1200,346 Q560,656 0,384Z" fill="#a6d22e"/>
      <path d="M0,384 Q560,656 1200,346 L1200,740 L0,740Z" fill="#27a3dd"/>
    </svg>
    <div class="hero-copy">
      <div class="hero-title">Easy Equipment Finance!<br>Fast Approvals to $50,000*</div>
      <div class="hero-rule"></div>
      <div class="hero-sub">Equipment Finance,Business Finance,Commercial Finance,<br>Construction Finance, Bridging Finance</div>
      <span class="btn btn-blue">Contact Us ✉</span>
    </div>
    <div class="callback"><h2>Get Funded Today, enter details below for a call back</h2></div>
    <div class="field" style="left:312px">Phone Number</div>
    <div class="field" style="left:606px">Email</div>
    <div class="cb-btn" style="left:380px;background:#fff;color:var(--blue)">Get A Call Back</div>
    <div class="cb-btn" style="left:606px;border:2px solid #fff;color:#fff">Apply online</div>
  </section>

  <!-- services -->
  <section class="abs services">
    <h2 class="section-title" style="margin-top:52px">Our Services</h2>
    <div class="service" style="left:108px">
      <div class="ring"><span><svg width="34" height="34" viewBox="0 0 34 34" aria-hidden="true"><circle cx="17" cy="17" r="11" fill="none" stroke="#fff" stroke-width="5" stroke-dasharray="4 3"/><circle cx="17" cy="17" r="7" fill="none" stroke="#fff" stroke-width="3"/></svg></span></div>
      <h3>Equipment Finance</h3>
      <p>Lorem Ipsum is simply dummy text of the printing and typesetting industry. Lorem Ipsum has been the industry's</p>
      <div class="divider"><b></b><i>+</i><b></b></div>
    </div>
    <div class="service" style="left:352px">
      <div class="ring"><span><svg width="30" height="30" viewBox="0 0 30 30" aria-hidden="true"><rect x="3" y="3" width="24" height="24" fill="none" stroke="#fff" stroke-width="2"/><rect x="8" y="15" width="3" height="8" fill="#fff"/><rect x="13" y="10" width="3" height="13" fill="#fff"/><rect x="18" y="13" width="3" height="10" fill="#fff"/></svg></span></div>
      <h3>Business Finance</h3>
      <p>Lorem Ipsum is simply dummy text of the printing and typesetting industry. Lorem Ipsum has been the industry's</p>
      <div class="divider"><b></b><i>+</i><b></b></div>
    </div>
    <div class="service" style="left:596px">
      <div class="ring"><span><svg width="34" height="30" viewBox="0 0 34 30" aria-hidden="true"><circle cx="20" cy="8" r="5" fill="#fff"/><path d="M2,20 L10,17 L20,19 L30,15 L32,18 L20,25 L2,25Z" fill="#fff"/></svg></span></div>
      <h3>Commercial Finance</h3>
      <p>Lorem Ipsum is simply dummy text of the printing and typesetting industry. Lorem Ipsum has been the industry's</p>
      <div class="divider"><b></b><i>+</i><b></b></div>
    </div>
    <div class="service" style="left:840px">
      <div class="ring"><span><svg width="32" height="28" viewBox="0 0 32 28" aria-hidden="true"><rect x="3" y="8" width="26" height="17" rx="2" fill="#fff"/><rect x="8" y="3" width="12" height="6" fill="#fff"/><rect x="21" y="13" width="8" height="6" fill="#27a3dd"/></svg></span></div>
      <h3>Compassionate</h3>
      <p>Lorem Ipsum is simply dummy text of the printing and typesetting industry. Lorem Ipsum has been the industry's</p>
      <div class="divider"><b></b><i>+</i><b></b></div>
    </div>
  </section>

  <!-- testimonials -->
  <section class="abs testimonials" role="img" aria-label="Dark photo of a handshake behind the testimonial">
    <h2 class="section-title">Testimonials</h2>
    <div class="avatar" role="img" aria-label="Portrait of the client"></div>
    <div class="t-name">Dane Orwell</div>
    <div class="t-role">Lorem Ipsum is simply dummy</div>
    <p class="t-quote">Lorem Ipsum is simply dummy text of the printing and typesetting industry. Lorem Ipsum has been the industry's standard dummy text ever since the 1500s, when an unknown printer took a galley of type and scrambled it to make a type specimen book. It has survived not only five centuries, but also the leap into electronic typesetting. Lorem Ipsum is simply dummy text of the printing printer took a</p>
    <svg class="arrow" style="left:130px;top:206px" viewBox="0 0 28 28" aria-hidden="true"><circle cx="14" cy="14" r="14" fill="#ccc"/><path d="M16,8 L10,14 L16,20" fill="none" stroke="#222" stroke-width="3"/></svg>
    <svg class="arrow" style="left:1038px;top:206px" viewBox="0 0 28 28" aria-hidden="true"><circle cx="14" cy="14" r="14" fill="#a6d22e"/><path d="M12,8 L18,14 L12,20" fill="none" stroke="#222" stroke-width="3"/></svg>
  </section>

  <!-- lease + tabs -->
  <section class="abs lease">
    <h3>Equipment Finance : Operating Lease</h3>
    <p>Being able to keep up with the latest equipment models, not having the hassle of disposing of obsolete gear, using up precious working capital and claiming payments as tax deductions are just a few of the benefits of choosing to use a finance option when next making a purchase. We are also specialists in all types of equipment lease options and will provide you with a range of choices each and every time.<br>Make the right decision today...</p>
    <div class="btn-row">
      <div class="btn-solid" style="width:212px">Speak with a specialist</div>
      <div class="btn-outline" style="width:226px">I am a supplier, learn more</div>
    </div>
  </section>
  <section class="abs tabs">
    <div class="tab-row"><span class="on">Invoice Factoring</span><span>Trade Finance</span><span>Business Loans</span></div>
    <div class="tab-body">
      <p>Access 85% of your existing and new invoice value within 24 hours. Waiting to be paid leaves you without cash in the bank and distracts from your focus to take on new opportunities. Pay bills and wages on time with funding that grows with your turnover and not your credit rating.</p>
      <p class="links">[Learn more] [Skip &amp; Apply for a quote]</p>
      <div class="btn-row" style="margin-top:44px"><div class="btn-solid" style="width:208px">Speak with a specialist</div></div>
    </div>
  </section>

  <!-- finance needs -->
  <section class="abs needs">
    <div class="needs-photo" role="img" aria-label="Photo of a businessman in a suit with arms folded"></div>
    <div class="needs-copy">
      <h2>We look after all of your finance needs</h2>
      <p>Take a minute to use our quick quote tool for a guide on your borrowing capacity, to compare loan rates and much more. Leave your details and one of our experienced team will call to discuss your situation at a time that suits you.</p>
      <ul><li>Equipment Finance</li><li>Business Finance</li><li>Commercial Finance</li><li>Construction Finance</li><li>Bridging Finance</li></ul>
      <p style="margin-top:12px">Award winning brokers, individually tailored loans and professional service from our experienced team. Contact Varoplend today for all of your finance needs.</p>
    </div>
  </section>

  <!-- clients -->
  <section class="abs clients">
    <h2>OUR CLIENT</h2>
    <div class="client" style="left:160px;top:140px">Amelle Délices</div>
    <div class="client" style="left:340px;top:140px">Brevik Motors</div>
    <div class="client" style="left:510px;top:140px">Harbour Equity Council</div>
    <div class="client" style="left:700px;top:140px">Estrel Lumen</div>
    <div class="client" style="left:860px;top:140px">Merry Orbit</div>
    <div class="client" style="left:160px;top:220px">Bench Crafted</div>
    <div class="client" style="left:340px;top:220px">Lorvique</div>
    <div class="client" style="left:510px;top:220px">Manterra Life</div>
    <div class="client" style="left:700px;top:220px">Mazuro</div>
    <div class="client" style="left:860px;top:220px">Melvaro</div>
    <svg class="arrow" style="left:132px;top:166px" viewBox="0 0 28 28" aria-hidden="true"><circle cx="14" cy="14" r="14" fill="#bbb"/><path d="M16,8 L10,14 L16,20" fill="none" stroke="#fff" stroke-width="3"/></svg>
    <svg class="arrow" style="left:1038px;top:166px" viewBox="0 0 28 28" aria-hidden="true"><circle cx="14" cy="14" r="14" fill="#1f5f7a"/><path d="M12,8 L18,14 L12,20" fill="none" stroke="#fff" stroke-width="3"/></svg>
  </section>

  <!-- blog -->
  <section class="abs blog">
    <h2>Our Blog</h2>
    <article class="post" style="left:135px">
      <div class="date"><b>18</b><span>Dec</span></div>
      <h4>Lorem Ipsum is simply dummy text of the</h4>
      <p>Lorem Ipsum is simply dummy text of the printing and typesetting industry. Lorem Ipsum has been the industry's standard dummy text ever since the 1500s, when an unknown printer took a galley of type and scrambled it to make a type</p>
    </article>
    <article class="post" style="left:622px">
      <div class="date"><b>19</b><span>Dec</span></div>
      <h4>Lorem Ipsum is simply dummy text of the</h4>
      <p>Lorem Ipsum is simply dummy text of the printing and typesetting industry. Lorem Ipsum has been the industry's standard dummy text ever since the 1500s, when an unknown printer took a galley of type and scrambled it to make a type</p>
    </article>
  </section>

  <!-- footer -->
  <footer class="abs footer">
    <svg width="1200" height="284" viewBox="0 0 1200 284" aria-hidden="true">
      <path d="M0,40 Q600,-20 1200,40 L1200,284 L0,284Z" fill="#a6d22e"/>
      <path d="M0,48 Q600,-8 1200,48 L1200,284 L0,284Z" fill="#27a3dd"/>
    </svg>
    <div class="brand footer-brand">
      <span class="brand-mark"></span>
      <span class="brand-name">Kestrel Equipment</span>
    </div>
    <div class="f-divider"></div>
    <div class="social"><i></i><i></i><i></i><i></i></div>
    <div class="f-mail">info@kestrel-adequip.com</div>
    <div class="f-rule"></div>
    <div class="f-nav"><span class="active">Home</span><span>Equipment Finance</span><span>Business Finance</span><span>Supplier Finance</span><span>Equip Blog</span><span>Contact Us</span></div>
    <div class="f-rule2"></div>
    <div class="copyright">Copyright 2016</div>
  </footer>

</div>
</body>
</html>
```